Looking for someone to design a business card for my plumbing business Brindle Plumbing Solutions I want the background also to be black, must attract clients. If possible I want the front to be the logo and the back to show maybe the details.

Target Market(s)

Clients

Industry/Entity Type

Plumbing maintenance

Contact Information for Business Card

Name: Dylan, Contact: 0451 306 729, Email: brindleplumbingsolutions@mailpost.example, Licence number 728094K

Font styles to use
Other font styles liked:
• as per logo maybe?

Colors

Designer to choose colors to be used in the design.

Requirements
Nice to have
• stating the service I provide, emergency plumbing, plumbing maintenance, drainage maintenance, block sewer and stormwater, camera and locating.

```html
<!DOCTYPE html>
<html lang="en">
<head>
<meta charset="utf-8">
<title>Brindle Plumbing Solutions — Business Card</title>
<link href="https://fonts.googleapis.com/css2?family=Montserrat:wght@400;500;700;800&display=swap" rel="stylesheet">
<style>
  :root {
    --page: #161616;
    --card: #232323;
    --card-back: #212121;
    --blue: #4a8fd0;
    --white: #f4f4f4;
    --text: #e8e8e8;
    --faint: #3b3b3b;
  }
  * { margin: 0; padding: 0; box-sizing: border-box; }
  html, body {
    width: 1200px; height: 1059px; overflow: hidden;
    background: var(--page);
    font-family: "Montserrat", sans-serif;
  }
  .canvas { position: relative; width: 1200px; height: 1059px; }
  .card {
    position: absolute; left: 256px; width: 688px; height: 392px;
    border-radius: 20px; overflow: hidden;
    box-shadow: 0 14px 30px rgba(0,0,0,.55);
  }
  .card--front { top: 89px; background: var(--card); }
  .card--back { top: 547px; background: var(--card-back); }

  .brand-mark {
    position: absolute; right: 40px; top: 88px;
    text-align: right; color: var(--white);
    font-weight: 800; font-size: 27px; line-height: 1.1;
    letter-spacing: .5px; text-transform: uppercase;
  }
  .person { position: absolute; left: 38px; top: 198px; }
  .person__name {
    color: var(--blue); font-weight: 700; font-size: 25px;
    letter-spacing: .3px; line-height: 1; text-transform: uppercase;
  }
  .person__role { color: var(--text); font-size: 15px; margin-top: 3px; }
  .divider {
    position: absolute; left: 38px; right: 40px; top: 258px;
    height: 1.5px; background: var(--blue);
  }
  .contacts { position: absolute; left: 38px; top: 276px; list-style: none; }
  .contacts li {
    display: flex; align-items: center; gap: 8px;
    color: var(--text); font-size: 15.5px; height: 26px;
  }
  .contacts svg { width: 13px; height: 13px; flex: none; }
  .band-white {
    position: absolute; left: 0; bottom: 0; width: 420px; height: 9px;
    background: var(--white);
    clip-path: polygon(0 0, 100% 0, 97.5% 100%, 0 100%);
  }
  .band-licence {
    position: absolute; right: 0; bottom: 0; width: 268px; height: 31px;
    background: var(--blue);
    clip-path: polygon(24px 0, 100% 0, 100% 100%, 0 100%);
    color: var(--white); font-size: 15px;
    display: flex; align-items: center; justify-content: center; padding-left: 18px;
  }

  .brand-mark--faint {
    position: absolute; left: 0; right: 0; top: 120px;
    text-align: center; color: var(--faint);
    font-weight: 800; font-size: 42px; line-height: 1.1;
    text-transform: uppercase; letter-spacing: 1px;
  }
  .services {
    position: absolute; left: 0; right: 0; top: 310px;
    text-align: center; color: var(--text); font-size: 15.5px; line-height: 27px;
  }
  .services .dot { color: var(--blue); margin: 0 7px; }
</style>
</head>
<body>
<main class="canvas">
  <section class="card card--front">
    <div class="brand-mark">Brindle<br>Plumbing Solutions</div>

    <div class="person">
      <div class="person__name">Dylan</div>
      <div class="person__role">Founder &amp; CEO</div>
    </div>
    <div class="divider"></div>

    <ul class="contacts">
      <li>
        <svg viewBox="0 0 24 24" aria-hidden="true"><path fill="#4a8fd0" d="M6.6 10.8a15.1 15.1 0 0 0 6.6 6.6l2.2-2.2a1 1 0 0 1 1-.25 11.4 11.4 0 0 0 3.6.57 1 1 0 0 1 1 1V20a1 1 0 0 1-1 1A17 17 0 0 1 3 4a1 1 0 0 1 1-1h3.5a1 1 0 0 1 1 1c0 1.25.2 2.45.57 3.57a1 1 0 0 1-.25 1z"/></svg>
        0451 306 729
      </li>
      <li>
        <svg viewBox="0 0 24 24" aria-hidden="true"><rect x="1" y="4" width="22" height="16" fill="#4a8fd0"/><path d="M1 4l11 9 11-9" fill="none" stroke="#232323" stroke-width="2"/></svg>
        brindleplumbingsolutions@mailpost.example
      </li>
      <li>
        <svg viewBox="0 0 24 24" aria-hidden="true"><circle cx="12" cy="12" r="11" fill="#4a8fd0"/></svg>
        @BrindlePlumbingSolutions
      </li>
    </ul>

    <div class="band-white"></div>
    <div class="band-licence">Licence number 728094K</div>
  </section>

  <section class="card card--back">
    <div class="brand-mark--faint">Brindle<br>Plumbing Solutions</div>
    <p class="services">
      Emergency plumbing<span class="dot">•</span>Plumbing maintenance<span class="dot">•</span>Drainage maintenance<br>
      Block sewer and stormwater<span class="dot">•</span>Camera and locating
    </p>
  </section>
</main>
</body>
</html>
```